Aquavell- plumbing service flyer

Hello,
We would like to create flyer for our plumbing company Aquavell
- we have 2 web domains
aquavell-zx.hr ( official)
uredjenjesobicazx.hr ( for bathroom renovation)

- we would like to create a similar Z-fold flyer ( from A4 paper) for our services
- We are sending images used on our websites. Of Course, it is allowed to put some of their own. Depending on design
- sending word with text which should go on each page. Text can be modified but in the sense of a page. The massage on a page should be as in word.
What is important to us:
- to stay in blue color
- It should be 1 page when fully open. So it looks like the complete page of information
- first/front page should be with our logo and phone number. more focus on emergency plumbing.
- back page should be about bathroom remodeling. Not necessary but would be received more points
- please don't use images of regular plumbers from Pixmarble and similar. we don't want to use this stock's regular images as all others.

Target Market(s)

Bathroom remodeling and emergency plumbing

Industry/Entity Type

Construction-Plumbing

Colors
0054AA
0677BA
7BADD7
CADEEF
E8F1F8

Requirements
Must have
• Logo

```html
<!DOCTYPE html>
<html lang="en">
<head>
<meta charset="utf-8">
<title>Aquavell – Plumbing Service Flyer</title>
<link rel="stylesheet" href="https://fonts.googleapis.com/css2?family=Bebas+Neue&family=Montserrat:wght@300;400;600;700;800&display=swap">
<style>
  :root {
    --navy: #154385;
    --sky: #4fb9e6;
    --amber: #fbb522;
    --signal-red: #fe0000;
    --white: #ffffff;
    --link-blue: #1f35a8;
    --mascot-light: #7fcdef;
    --mascot-deep: #2f8fd6;
  }
  * { margin: 0; padding: 0; box-sizing: border-box; }
  html, body { width: 1200px; height: 824px; overflow: hidden; background: var(--white); }
  .flyer {
    position: relative; width: 1200px; height: 824px;
    display: grid; grid-template-columns: 386px 427px 387px;
    font-family: "Montserrat", Arial, sans-serif; color: var(--white);
  }
  .panel { position: relative; overflow: hidden; }
  .panel + .panel { border-left: 1px solid rgba(255,255,255,0.25); }
  .panel-bg { position: absolute; inset: 0; width: 100%; height: 100%; }
  .display { font-family: "Bebas Neue", Impact, sans-serif; font-weight: 400; line-height: 1; }

  /* Left panel */
  .brand-title { position: absolute; left: 36px; top: 34px; font-size: 78px; letter-spacing: 0.5px; }
  .mascot-art {
    position: absolute; left: 62px; top: 604px; width: 330px; height: 330px; border-radius: 50%;
    background: radial-gradient(circle at 50% 40%, var(--mascot-light) 0%, var(--mascot-deep) 75%);
    opacity: 0.55;
  }
  .intro { position: absolute; left: 25px; top: 153px; width: 345px; font-weight: 600; font-size: 16.6px; line-height: 23.7px; }
  .intro p + p { margin-top: 23.7px; }
  .service-list { list-style: none; font-size: 14px; line-height: 23.7px; margin-top: 24px; }
  .tagline { margin-top: 24px; }

  /* Middle panel */
  .middle { background: var(--navy); text-align: center; }
  .emergency-title { margin-top: 42px; font-size: 54px; letter-spacing: -0.5px; }
  .emergency-title .accent { color: var(--sky); }
  .emergency-sub { margin-top: 39px; color: var(--amber); font-weight: 600; font-size: 33px; }
  .emergency-list { list-style: none; margin-top: 32px; font-weight: 600; font-size: 25.5px; line-height: 35.3px; }
  .team-note { font-weight: 600; font-size: 25.5px; line-height: 35.3px; }
  .cta-box {
    position: absolute; left: 36px; top: 679px; width: 355px; height: 104px;
    background: var(--signal-red); padding-top: 14px;
  }
  .cta-title { font-size: 54px; }
  .cta-sub { margin-top: 4px; font-weight: 700; font-size: 24px; }

  /* Right panel */
  .right { text-align: center; }
  .logo-block { position: absolute; left: 0; right: 0; top: 30px; display: flex; flex-direction: column; align-items: center; }
  .logo-dot { width: 170px; height: 170px; border-radius: 50%; background: var(--sky); }
  .logo-name { margin-top: 16px; font-weight: 800; font-size: 44px; letter-spacing: 1px; }
  .services-title { position: absolute; left: 0; right: 0; top: 329px; font-size: 52px; }
  .services-list { position: absolute; left: 0; right: 0; top: 390px; list-style: none; font-weight: 700; font-size: 23px; line-height: 35.4px; }
  .services-list li::before {
    content: ""; display: inline-block; width: 13px; height: 13px; border-radius: 50%;
    background: var(--sky); margin-right: 6px; vertical-align: 3px;
  }
  .phone { position: absolute; left: 0; right: 0; top: 553px; font-size: 62px; }
  .contact { position: absolute; left: 0; right: 0; top: 704px; font-size: 20px; line-height: 36.5px; }
  .contact .email { font-weight: 300; }
  .contact a { display: block; color: var(--link-blue); text-decoration: underline; font-weight: 400; }
</style>
</head>
<body>
<main class="flyer">

  <section class="panel left">
    <svg class="panel-bg" viewBox="0 0 386 824" preserveAspectRatio="none" aria-hidden="true">
      <rect width="386" height="824" fill="var(--sky)"/>
      <path d="M0 0 H386 V107 Q220 165 0 150 Z" fill="var(--amber)"/>
      <path d="M0 0 H386 V63 Q220 140 0 126 Z" fill="var(--navy)"/>
    </svg>
    <div class="mascot-art" role="img" aria-label="Illustration of the Aquavell plumber mascot holding a pipe and giving a thumbs up"></div>
    <h1 class="brand-title display">AQUAVELL</h1>
    <div class="intro">
      <p>Do you need a plumber for bathroom renovation? Did your pipe burst or have some clogging in pipes ? The neighbor's has ceiling leak?<br>We offer plumbing services in the area of the City of Zagreb and its surroundings.</p>
      <p>Some of the common plumbing services include:</p>
      <ul class="service-list">
        <li>1.Installation of new plumbing systems</li>
        <li>2.Repair of leaking pipes, faucets, and fixtures</li>
        <li>3. Drain cleaning and unclogging</li>
        <li>4. Sewer line repair and replacement</li>
        <li>5. Bathroom and kitchen plumbing installation and repair</li>
      </ul>
      <p class="tagline">Reliability, speed, accessibility.<br>Your Aquavell.</p>
    </div>
  </section>

  <section class="panel middle">
    <h2 class="emergency-title display">EMERGENCY <span class="accent">PLUMBING</span></h2>
    <p class="emergency-sub">Emergency services:</p>
    <ul class="emergency-list">
      <li>- mechanical drain cleaning</li>
      <li>- water jet pipe cleaning</li>
      <li>- leak detections</li>
      <li>- pipe inspection with<br>camera</li>
      <li>- thermal imaging of leakes</li>
      <li>- main pipe check up</li>
      <li>- valve change</li>
      <li>- change of sink siphon</li>
    </ul>
    <p class="team-note">Aquavell team will help you<br>to manage all the plumbing<br>crises.</p>
    <div class="cta-box">
      <p class="cta-title display">FAST AND RELIABLE</p>
      <p class="cta-sub">CONTACT US DAILY 24/7</p>
    </div>
  </section>

  <section class="panel right">
    <svg class="panel-bg" viewBox="0 0 387 824" preserveAspectRatio="none" aria-hidden="true">
      <rect width="387" height="824" fill="var(--sky)"/>
      <path d="M0 0 H387 V645 Q220 700 0 691 Z" fill="var(--amber)"/>
      <path d="M0 0 H387 V604 Q220 675 0 666 Z" fill="var(--navy)"/>
    </svg>
    <div class="logo-block">
      <div class="logo-dot" aria-hidden="true"></div>
      <p class="logo-name">AQUAVELL</p>
    </div>
    <h2 class="services-title display">SERVICES :</h2>
    <ul class="services-list">
      <li>BATHROOM REMODELING</li>
      <li>EMERGENCY PLUMBING</li>
      <li>PLUMBING</li>
      <li>LEK DETECTION</li>
    </ul>
    <p class="phone display">+385 91 555 0142</p>
    <div class="contact">
      <p class="email">info@aquavell-zx.hr</p>
      <a href="#">www.aquavell-zx.com</a>
      <a href="#">www.uredjenjesobicazx.hr</a>
    </div>
  </section>

</main>
</body>
</html>
```